Wedding Invitation and Logo

We would like an invitation and logo designed for our wedding on October 19, 2019 in Charlotte, NC. Our names are Tess and Hank, we met in school at Brindlewood Ridge University, and we got engaged at a fire tower which has a view down to the campus. You do not have to include these, but some ideas for the invitation design would be mountains, a fire tower, our initials, or the city. The wedding will be at 4:30 in the afternoon with a reception to follow. We do not need to list the families as there are four of them and that is too much info. The colors we would like to use are white, black, royal blue, and maybe silver. Do not feel obligated to use them all though.We would like the logo to include similar elements such as mountains, fire tower, or our initials(T and H). The logo can be a one color design as we may use it on our cake, as light filters to be displayed on the walls at our reception, or as an accent on name plates and stationery.We like simple, clean designs and our wedding will have a wintery theme (white linens, white chair covers, silver and royal blue accents, etc.).Things we do not want: snowflakes, flowers, polka dots, leaves, gold foil.Thank you!

Font styles to use
Serif
Script

Requirements
Must have
• Some combination of white, black, royal blue, optionally silver.
Nice to have
• Mountains, fire tower, our initials (T and H), wintry theme (no snowflakes)
Should not have
• Snowflakes, flowers, polka dots, leaves, gold foil

```html
<!DOCTYPE html>
<html lang="en">
<head>
<meta charset="utf-8">
<title>Tess and Hank – Wedding Invitation</title>
<link rel="stylesheet" href="https://fonts.googleapis.com/css2?family=Courier+Prime:wght@400;700&family=UnifrakturMaguntia&display=swap">
<style>
  :root {
    --backdrop: #e4e5e7;
    --card: #ffffff;
    --ink-white: #ffffff;
    --navy: #1a1f6e;
    --royal: #1f56a8;
    --sky: #4d8fd0;
    --mist: #c9dcf1;
    --reception-blue: #2f62a5;
  }
  html, body {
    margin: 0;
    padding: 0;
    width: 1200px;
    height: 1200px;
    overflow: hidden;
    background: var(--backdrop);
  }
  .invitation {
    position: absolute;
    left: 186px;
    top: 56px;
    width: 786px;
    height: 1096px;
    background: var(--card);
    overflow: hidden;
    box-shadow: 0 2px 10px rgba(0,0,0,0.12);
  }
  .wash {
    position: absolute;
    inset: 0;
    width: 786px;
    height: 1096px;
  }
  .line {
    position: absolute;
    left: 0;
    width: 786px;
    text-align: center;
    margin: 0;
    color: var(--ink-white);
    white-space: nowrap;
  }
  .intro {
    font-family: "Courier Prime", "Courier New", monospace;
    font-size: 19px;
    line-height: 24px;
    left: -8px;
  }
  .intro.first { top: 214px; }
  .intro.second { top: 238px; }
  .name {
    font-family: "UnifrakturMaguntia", serif;
    font-size: 190px;
    line-height: 1;
    width: auto;
    text-align: left;
  }
  .name.bride { left: 86px; top: 250px; }
  .name.groom { left: 332px; top: 470px; }
  .conjunction {
    font-family: "UnifrakturMaguntia", serif;
    font-size: 46px;
    line-height: 1;
    left: 362px;
    top: 434px;
    width: auto;
    letter-spacing: 4px;
  }
  .date {
    font-family: "Courier Prime", "Courier New", monospace;
    font-size: 46px;
    top: 656px;
    left: -22px;
  }
  .time {
    font-family: "Courier Prime", "Courier New", monospace;
    font-size: 32px;
    top: 704px;
    left: -22px;
  }
  .place {
    font-family: "Courier Prime", "Courier New", monospace;
    font-size: 25px;
    top: 740px;
    left: -22px;
  }
  .reception {
    font-family: "Courier Prime", "Courier New", monospace;
    font-size: 28px;
    color: var(--reception-blue);
    top: 922px;
    left: -22px;
  }
</style>
</head>
<body>
  <main class="invitation">
    <svg class="wash" viewBox="0 0 786 1096" role="img" aria-label="Blue watercolour wash, deep navy at the centre fading to pale blue and white at the edges">
      <defs>
        <radialGradient id="ink-core" cx="0.55" cy="0.42" r="0.62">
          <stop offset="0" stop-color="var(--navy)"/>
          <stop offset="0.38" stop-color="#1d2f8a"/>
          <stop offset="0.7" stop-color="var(--royal)"/>
          <stop offset="1" stop-color="var(--sky)"/>
        </radialGradient>
        <radialGradient id="pale-wash" cx="0.5" cy="0.45" r="0.6">
          <stop offset="0" stop-color="#a9c8ea"/>
          <stop offset="0.7" stop-color="var(--mist)"/>
          <stop offset="1" stop-color="#ffffff" stop-opacity="0"/>
        </radialGradient>
      </defs>
      <path d="M10 40 C120 0 300 10 420 30 C560 10 700 20 786 40 L786 1000 C660 1060 480 1040 360 1060 C220 1090 90 1040 10 1000 Z" fill="url(#pale-wash)"/>
      <path d="M20 190 C60 120 150 160 230 120 C280 60 360 90 440 70 C520 30 620 50 700 40 C760 60 786 70 786 90 L786 760 C760 800 720 840 660 850 C600 900 520 880 460 900 C390 920 330 880 270 870 C200 860 150 810 110 760 C50 720 30 650 20 560 C10 460 0 300 20 190 Z" fill="url(#ink-core)"/>
    </svg>

    <p class="line intro first">together with their families</p>
    <p class="line intro second">Invite Your To Our Wedding</p>
    <p class="line name bride">Tess</p>
    <p class="line conjunction">AND</p>
    <p class="line name groom">Hank</p>
    <p class="line date">10.19.2019</p>
    <p class="line time">4.30 PM</p>
    <p class="line place">Charlotte, North Carolina</p>
    <p class="line reception">Reception to follow</p>
  </main>
</body>
</html>
```